CEDARWICK RESTASURANT WINE LIST - REDESIGN/REFORMAT

Need a menu redesign/resizing of our wine list/beverage menu from standard letter size to a 4.25 x 11 inch “Drink Menu” size. Could do with a nicer cover page. Wine list, descriptions, pricing, almost all stays the same minus the formatting and possibly new cover page/font.

Few minor edits need to be made to descriptions and pricing on wine and beer list.

Someone competent in illustrator should be able to get this done in literal hours, and I don’t find myself having the time, and less know how than someone here!

Need sent back in PDF Format so i can send to local print shop.

Thanks in advance

Target Market(s)

Our restaurants's customers/patrons

Colors

Designer to choose only greyscale colors for use in the design.

Requirements
Must have
• A few text edits sent in before final edit. please PM so i can tell you what aspects of the wine list/beer menu need to be edited.
Nice to have
• Elegant font but readable

```html
<!DOCTYPE html>
<html lang="en">
<head>
<meta charset="utf-8">
<title>Cedarwick Restaurant – Wine List</title>
<link href="https://fonts.googleapis.com/css2?family=Playfair+Display:wght@700;800&family=Cormorant+Garamond:ital,wght@0,400;0,500;0,600;1,500;1,600&display=swap" rel="stylesheet">
<style>
  :root{
    --backdrop:#e6e6e6;
    --paper:#ffffff;
    --ink:#1e1e1e;
    --ink-soft:#555555;
    --rule:#9a9a9a;
  }
  *{box-sizing:border-box;margin:0;padding:0}
  html,body{width:1200px;height:2544px;overflow:hidden;background:var(--backdrop)}
  body{position:relative;font-family:"Cormorant Garamond",Georgia,serif;color:var(--ink)}
  .page{position:absolute;width:480px;height:1240px;background:var(--paper);box-shadow:0 2px 8px rgba(0,0,0,.12);padding:70px 44px 40px}
  .p1{left:60px;top:22px}.p2{left:660px;top:22px}.p3{left:60px;top:1282px}.p4{left:660px;top:1282px}

  /* cover */
  .cover{display:flex;flex-direction:column;align-items:center;justify-content:space-between;padding:0}
  .brand{margin-top:500px;text-align:center}
  .brand-name{font-family:"Playfair Display",Georgia,serif;font-weight:800;font-size:46px;letter-spacing:1px}
  .brand-sub{font-size:14px;letter-spacing:4px;margin-top:2px}
  .cover-foot{margin-bottom:110px;text-align:center;font-size:15px;letter-spacing:2px;line-height:1.4}

  .page-title{text-align:right;font-size:15px;font-weight:600;letter-spacing:2px;line-height:1.25;margin-bottom:26px}
  .page-title::after{content:"";display:block;width:150px;height:1px;background:var(--rule);margin:8px 0 0 auto}
  .col-head{display:flex;justify-content:flex-end;gap:14px;font-size:9px;font-style:italic;color:var(--ink-soft)}
  .section{margin-bottom:14px}
  .section h3{font-style:italic;font-weight:600;font-size:13px;border-bottom:1px solid var(--rule);display:flex;justify-content:space-between;align-items:flex-end;padding-bottom:1px;margin-bottom:4px}
  .item{display:flex;justify-content:space-between;font-size:9.5px;font-weight:600;line-height:1.3}
  .item .pr{display:flex;gap:16px;min-width:48px;justify-content:flex-end}
  .desc{font-size:8.5px;font-style:italic;color:var(--ink-soft);line-height:1.25;margin-bottom:5px;padding-right:60px}
  .foot{position:absolute;left:44px;right:44px;bottom:54px;text-align:center;font-size:8.5px;font-style:italic;color:var(--ink-soft);line-height:1.35}
  .sub{font-size:9.5px;font-style:italic;font-weight:600;margin:4px 0 2px}
</style>
</head>
<body>

<section class="page p1 cover">
  <div class="brand">
    <div class="brand-name">CEDARWICK</div>
    <div class="brand-sub">RESTAURANT</div>
  </div>
  <div class="cover-foot">WINE LIST<br>BEVERAGE MENU</div>
</section>

<section class="page p2">
  <h2 class="page-title">WHITE WINES<br>&amp; BUBBLES</h2>
  <div class="section"><h3>Chardonnay <span class="col-head"><span>Glass</span><span>Bottle</span></span></h3>
    <div class="item"><span>2021 Meadowlark Valley · Sonoma, California</span><span class="pr"><span>12</span><span>44</span></span></div>
    <div class="desc">Full of ripe pear, baked apple and a hint of toasted oak</div>
    <div class="item"><span>2022 Harbor Crest · Central Coast, California</span><span class="pr"><span></span><span>52</span></span></div>
    <div class="desc">Notes of lemon curd, vanilla and a round buttery finish</div></div>
  <div class="section"><h3>Albariño</h3>
    <div class="item"><span>2022 Alta Rías · Galicia, Spain</span><span class="pr"><span>11</span><span>40</span></span></div>
    <div class="desc">Crisp stone fruit with a bright saline finish</div>
    <div class="item"><span>2021 Quinta Verde · Minho, Portugal</span><span class="pr"><span></span><span>38</span></span></div>
    <div class="desc">Zesty citrus, green apple and fresh floral notes</div></div>
  <div class="section"><h3>Pinot Grigio</h3>
    <div class="item"><span>2022 Villa Serena · Veneto, Italy</span><span class="pr"><span>10</span><span>36</span></span></div>
    <div class="desc">Light and clean with white peach and almond</div></div>
  <div class="section"><h3>Riesling</h3>
    <div class="item"><span>2021 Stonebridge · Finger Lakes, New York</span><span class="pr"><span>11</span><span>40</span></span></div>
    <div class="desc">Off-dry with apricot, honeysuckle and lively acidity</div></div>
  <div class="section"><h3>Rosé</h3>
    <div class="item"><span>2022 Maison Lavande · Provence, France</span><span class="pr"><span>12</span><span>44</span></span></div>
    <div class="desc">Pale pink, dry and delicate with strawberry and melon</div></div>
  <div class="section"><h3>Sauvignon Blanc</h3>
    <div class="item"><span>2022 Southern Tide · Marlborough, New Zealand</span><span class="pr"><span>11</span><span>40</span></span></div>
    <div class="desc">Passion fruit, lime zest and fresh cut grass</div>
    <div class="item"><span>2021 Clos Argent · Loire Valley, France</span><span class="pr"><span></span><span>48</span></span></div>
    <div class="desc">Flinty minerality with grapefruit and white flowers</div></div>
  <div class="section"><h3>Champagne &amp; Sparkling Wines</h3>
    <div class="item"><span>NV Brut Prosecco · Treviso, Italy</span><span class="pr"><span>10</span><span>36</span></span></div>
    <div class="desc">Persistent fine bubbles, green apple and pear</div>
    <div class="item"><span>NV Brut Rosé · Crémant de Loire, France</span><span class="pr"><span></span><span>54</span></span></div>
    <div class="desc">Red berries, brioche and a creamy finish</div>
    <div class="item"><span>NV Maison Dufort Brut · Champagne, France</span><span class="pr"><span></span><span>98</span></span></div>
    <div class="desc">Toasted almond, citrus peel and elegant mousse</div>
    <div class="item"><span>2016 Grand Réserve · Champagne, France</span><span class="pr"><span></span><span>160</span></span></div></div>
  <p class="foot">Enjoy 50% off bottled wines and sake every Wednesday.<br>Bottle corkage subject to change. Corkage fee $15 per bottle.<br>No outside bottles purchased from our wine list.<br>Ask your server for today's by-the-glass features.</p>
</section>

<section class="page p3">
  <h2 class="page-title">RED WINES</h2>
  <div class="section"><h3>Barbera <span class="col-head"><span>Glass</span><span>Bottle</span></span></h3>
    <div class="item"><span>2020 Poggio Alto · Piedmont, Italy</span><span class="pr"><span>12</span><span>44</span></span></div>
    <div class="desc">Bright cherry and plum with soft tannins</div></div>
  <div class="section"><h3>Cabernet Sauvignon</h3>
    <div class="item"><span>2020 Redstone Ridge · Paso Robles, California</span><span class="pr"><span>14</span><span>52</span></span></div>
    <div class="desc">Blackcurrant, cedar and a firm structured finish</div>
    <div class="item"><span>2019 Oak Hollow · Napa Valley, California</span><span class="pr"><span></span><span>84</span></span></div>
    <div class="desc">Dark fruit, mocha and polished tannins</div></div>
  <div class="section"><h3>Merlot</h3>
    <div class="item"><span>2020 Willow Bend · Columbia Valley, Washington</span><span class="pr"><span>12</span><span>44</span></span></div>
    <div class="desc">Plush black cherry, cocoa and soft spice</div></div>
  <div class="section"><h3>Malbec</h3>
    <div class="item"><span>2021 Alto Andes · Mendoza, Argentina</span><span class="pr"><span>11</span><span>40</span></span></div>
    <div class="desc">Blackberry, violet and a velvety smooth body</div></div>
  <div class="section"><h3>Tempranillo</h3>
    <div class="item"><span>2019 Bodega Cerro · Rioja, Spain</span><span class="pr"><span></span><span>46</span></span></div>
    <div class="desc">Red fruit, leather and vanilla from oak aging</div></div>
  <div class="section"><h3>Zinfandel</h3>
    <div class="item"><span>2020 Old Vine Reserve · Lodi, California</span><span class="pr"><span>12</span><span>44</span></span></div>
    <div class="desc">Jammy raspberry, black pepper and warm spice</div></div>
  <div class="section"><h3>Pinot Noir</h3>
    <div class="item"><span>2021 Foggy Point · Willamette Valley, Oregon</span><span class="pr"><span>14</span><span>54</span></span></div>
    <div class="desc">Silky texture with cranberry and earthy notes</div>
    <div class="item"><span>2020 Coastal Hills · Sonoma Coast, California</span><span class="pr"><span></span><span>62</span></span></div>
    <div class="desc">Ripe cherry, rose petal and gentle oak</div></div>
  <div class="section"><h3>Red Blend</h3>
    <div class="item"><span>2020 Ironwood Estate · Paso Robles, California</span><span class="pr"><span>13</span><span>48</span></span></div>
    <div class="desc">Blend of syrah, grenache and mourvèdre</div>
    <div class="item"><span>2019 Château Belle Rive · Bordeaux, France</span><span class="pr"><span></span><span>70</span></span></div>
    <div class="desc">Blend of merlot and cabernet franc</div></div>
  <p class="foot">Enjoy 50% off bottled wines and sake every Wednesday.<br>Bottle corkage subject to change. Corkage fee $15 per bottle.<br>No outside bottles purchased from our wine list.</p>
</section>

<section class="page p4">
  <h2 class="page-title">SAKES, BEERS,<br>&amp; NON-ALCOHOLIC</h2>
  <div class="section"><h3>House Sake <span class="col-head"><span>Small</span><span>Large</span></span></h3>
    <div class="item"><span>Hot or Cold House Sake</span><span class="pr"><span>8</span><span>14</span></span></div>
    <div class="desc">Light and smooth, served warm or chilled</div></div>
  <div class="section"><h3>Plum Wine · 1.5 Liter <span class="col-head"><span>Glass</span><span>Bottle</span></span></h3>
    <div class="item"><span>Umeshu House Plum Wine</span><span class="pr"><span>8</span><span>42</span></span></div>
    <div class="desc">Sweet and fragrant with ripe plum</div></div>
  <div class="section"><h3>Premium Cold Sakes &amp; Sparkling Sake</h3>
    <div class="sub">Small Bottle · 300ml</div>
    <div class="item"><span>Snow Valley Junmai</span><span class="pr"><span>22</span></span></div>
    <div class="desc">Crisp and dry with a clean rice finish</div>
    <div class="item"><span>Moonlit River Ginjo</span><span class="pr"><span>26</span></span></div>
    <div class="desc">Melon and pear with a soft floral aroma</div>
    <div class="item"><span>Silver Bloom Daiginjo</span><span class="pr"><span>34</span></span></div>
    <div class="desc">Elegant and silky with delicate fruit</div>
    <div class="item"><span>Sparkling Sakura Sake</span><span class="pr"><span>18</span></span></div>
    <div class="sub">Large Bottle · 720ml</div>
    <div class="item"><span>Mountain Spring Nigori</span><span class="pr"><span>48</span></span></div>
    <div class="desc">Unfiltered, creamy and lightly sweet</div>
    <div class="item"><span>Crane Peak Junmai Ginjo</span><span class="pr"><span>56</span></span></div></div>
  <div class="section"><h3>On Draft <span class="col-head"><span>Pint</span><span>Pitcher</span></span></h3>
    <div class="item"><span>Harbor Light Lager</span><span class="pr"><span>7</span><span>22</span></span></div>
    <div class="item"><span>West Ridge IPA</span><span class="pr"><span>8</span><span>24</span></span></div>
    <div class="item"><span>Seasonal Craft Ale</span><span class="pr"><span>8</span><span>24</span></span></div></div>
  <div class="section"><h3>Bottled Beers</h3>
    <div class="item"><span>Rice Lager</span><span class="pr"><span>6</span></span></div>
    <div class="item"><span>Pale Ale</span><span class="pr"><span>6</span></span></div>
    <div class="item"><span>Amber Ale</span><span class="pr"><span>6</span></span></div>
    <div class="item"><span>Hard Cider</span><span class="pr"><span>7</span></span></div></div>
  <div class="section"><h3>Non-Alcoholic Beverages</h3>
    <div class="item"><span>Sparkling Mineral Water</span><span class="pr"><span>5</span></span></div>
    <div class="item"><span>Soft Drinks · Cola, Lemon-Lime, Ginger Ale</span><span class="pr"><span>3</span></span></div>
    <div class="item"><span>Iced Tea · Lemonade</span><span class="pr"><span>3</span></span></div>
    <div class="item"><span>Fresh Juice · Orange, Apple, Cranberry</span><span class="pr"><span>4</span></span></div>
    <div class="item"><span>Hot Tea · Green, Jasmine, Black</span><span class="pr"><span>3</span></span></div></div>
  <p class="foot">Enjoy 50% off bottled wines and sake every Wednesday.<br>Bottle corkage subject to change. Corkage fee $15 per bottle.<br>No outside bottles purchased from our wine list.</p>
</section>

</body>
</html>
```